Harrowgate Legal

To update and modernize current business card appearance. Marisa's business is based in Melbourne with 4 other lawyers in the firm. Marisa travels to the Pilbara in Western Australia approximately 1 week a month as part of the firms legal work. She consults with clients in Newman, Tom Price and Port Hedland. The lawyers work mostly from a home office, apart from court appearances. They have a virtual office in Melbourne city, and use facilities in 3 or 4 other locations around Melbourne. It is important the client's think this is a conventional law firm with a permanent office. Our business structure is a difficult concept for them to grasp. The business has been operational for 3 years, growing from 1 lawyer to 4 lawyers during that time. Our website is www.Harrowgatelegal.com.au and is currently being upgraded as we are not happy with its content. The logo is currently orange and dark grey but the orange is a difficult colour to reproduce and often turns out "poo" brown when documents are printed. We need clients to know we are user friendly and caring - and not head up our rears ends as some lawyers appear to be.
Updates

Thank you for the feedback so far. 1. Some of the designs have too much black (We prefer darker grey & not too much.) 2. Happy for designers to play around with different colours & logo design. What we're after is a modern look and business card that people say "wow" when they pick it up.

Industry/Entity Type

Business

```html
<!DOCTYPE html>
<html lang="en">
<head>
<meta charset="utf-8">
<title>Harrowgate Legal – Business Card</title>
<link rel="stylesheet" href="https://fonts.googleapis.com/css2?family=Crimson+Pro:wght@400;600&family=Open+Sans:wght@400;700&display=swap">
<style>
  :root {
    --accent: #d2462b;
    --charcoal: #4d4d4f;
    --ink: #3f3f41;
    --card: #f2f2f0;
    --backdrop: #e4e1dc;
    --white: #ffffff;
  }
  * { box-sizing: border-box; margin: 0; padding: 0; }
  html, body { width: 1200px; height: 900px; overflow: hidden; }
  body {
    background: var(--backdrop);
    font-family: "Open Sans", Arial, sans-serif;
    color: var(--ink);
  }
  .stage {
    position: relative;
    width: 1200px;
    height: 900px;
    display: flex;
    justify-content: center;
    align-items: center;
    gap: 80px;
  }
  .card {
    position: relative;
    width: 330px;
    height: 540px;
    background: var(--card);
    box-shadow: 0 6px 18px rgba(0,0,0,0.18);
    overflow: hidden;
  }

  /* brand name block */
  .brand {
    display: flex;
    align-items: center;
    gap: 10px;
  }
  .brand-dot {
    width: 18px;
    height: 18px;
    border-radius: 50%;
    background: var(--accent);
    flex: none;
  }
  .brand-name {
    font-family: "Crimson Pro", Georgia, serif;
    font-weight: 400;
    font-size: 27px;
    color: var(--charcoal);
    letter-spacing: 0.5px;
  }

  /* front */
  .front .brand { position: absolute; left: 34px; top: 52px; }
  .person { position: absolute; left: 34px; top: 158px; right: 30px; }
  .person-name {
    font-weight: 700;
    font-size: 19px;
    letter-spacing: 0.4px;
    color: var(--charcoal);
    text-transform: uppercase;
  }
  .person-credentials { font-size: 12.5px; margin-top: 4px; color: #6a6a6c; }
  .person-role { font-size: 18px; margin-top: 2px; color: var(--charcoal); }
  .divider {
    position: absolute;
    left: 34px;
    right: 30px;
    top: 270px;
    height: 1.5px;
    background: var(--accent);
  }
  .contacts {
    position: absolute;
    left: 34px;
    top: 296px;
    list-style: none;
    font-size: 13.5px;
    line-height: 1.55;
    color: var(--charcoal);
  }
  .contact-key { color: var(--accent); display: inline-block; width: 18px; }
  .location-band {
    position: absolute;
    left: 0; right: 0; bottom: 0;
    height: 128px;
    background: var(--charcoal);
    color: var(--white);
    padding: 34px 34px 0;
    font-size: 17px;
    line-height: 1.4;
  }

  /* back */
  .pillars {
    position: absolute;
    left: 40px;
    top: 40px;
    list-style: none;
    font-family: "Crimson Pro", Georgia, serif;
    font-size: 18px;
    letter-spacing: 1.2px;
    line-height: 1.3;
    text-transform: uppercase;
    color: var(--charcoal);
  }
  .pillars li::before { content: "• "; }
  .services-band {
    position: absolute;
    left: 0; right: 0;
    top: 150px;
    height: 210px;
    background: var(--accent);
    color: var(--white);
    font-family: "Crimson Pro", Georgia, serif;
    text-align: center;
    padding-top: 36px;
    list-style: none;
    font-size: 17px;
    line-height: 1.45;
  }
  .service-major { font-variant: small-caps; font-weight: 600; font-size: 19px; letter-spacing: 0.6px; }
  .firm-email {
    position: absolute;
    left: 40px;
    top: 392px;
    font-family: "Crimson Pro", Georgia, serif;
    font-size: 15px;
    color: var(--charcoal);
  }
  .back .brand { position: absolute; right: 32px; bottom: 46px; }
  .back .brand-name { font-size: 24px; }
</style>
</head>
<body>
  <main class="stage">
    <article class="card front">
      <div class="brand">
        <span class="brand-dot"></span>
        <span class="brand-name">Harrowgate Legal</span>
      </div>
      <div class="person">
        <h1 class="person-name">J. Marisa Thornton</h1>
        <p class="person-credentials">LLB (Hons) - Accredited Mediator</p>
        <p class="person-role">Principal Solicitor</p>
      </div>
      <div class="divider"></div>
      <ul class="contacts">
        <li><span class="contact-key">T</span>1300 Harrowgate (427 764)</li>
        <li><span class="contact-key">M</span>0412 555 019</li>
        <li><span class="contact-key">E</span>marisa.thornton@harrowgatelegal.com.au</li>
      </ul>
      <div class="location-band">
        <p>MELBOURNE</p>
        <p>Eastern and Bayside Suburbs</p>
      </div>
    </article>

    <article class="card back">
      <ul class="pillars">
        <li>Experience</li>
        <li>Support</li>
        <li>Solutions</li>
      </ul>
      <ul class="services-band">
        <li class="service-major">• Family Law •</li>
        <li>Collaborative Practice</li>
        <li>Mediation &amp; Negotiation</li>
        <li>Intervention Orders</li>
        <li class="service-major">• Criminal Law •</li>
      </ul>
      <p class="firm-email">info@harrowgatelegal.com.au</p>
      <div class="brand">
        <span class="brand-dot"></span>
        <span class="brand-name">Harrowgate Legal</span>
      </div>
    </article>
  </main>
</body>
</html>
```